Flyer for the Harvest Lantern Gathering 2018

Design a flyer for our annual conference with basic information about the conference: conference logo and year,

Location:
Dunmore Community Center (Downtown Portland)
482 Willowby Street, Portland, ME 04117,

Date:
August 24th, 25th and 26th, 2018
Start time 6:00PM

I would like the following three words added to the flyer. These words describe the vision of the conference:
Prophetic, Worship, Prayer

```html
<!DOCTYPE html>
<html lang="en">
<head>
<meta charset="utf-8">
<title>Harvest Lantern Gathering 2018 – Flyer</title>
<link rel="stylesheet" href="https://fonts.googleapis.com/css2?family=Jost:wght@500;600&family=Oswald:wght@400;500&family=Open+Sans:wght@400&display=swap">
<style>
  :root {
    --orange: #f39a1e;
    --orange-deep: #e8890f;
    --ink: #111111;
    --grey-text: #4a4a4a;
    --grey-label: #6b6b6b;
    --rule: #d9d9d9;
    --paper: #ffffff;
    --sky-dark: #2a1a10;
    --sky-mid: #7a4a22;
    --sky-glow: #e0a25a;
  }
  * { box-sizing: border-box; margin: 0; padding: 0; }
  html, body { width: 707px; height: 1200px; overflow: hidden; background: var(--paper); }
  .flyer { position: relative; width: 707px; height: 1200px; background: var(--paper); font-family: "Open Sans", Arial, sans-serif; }

  .hero { position: absolute; top: 0; left: 0; width: 707px; height: 560px; }
  .hero svg { display: block; }
  .hero__title {
    position: absolute; top: 34px; left: 0; width: 100%;
    text-align: center; color: #fff;
    font-family: "Jost", "Futura", sans-serif; font-weight: 600;
    font-size: 45px; line-height: 1.08; letter-spacing: 1px;
  }

  .badge {
    position: absolute; left: 258px; top: 440px; width: 190px; height: 190px;
    border-radius: 50%; background: var(--ink); border: 7px solid var(--paper);
    box-shadow: 0 2px 6px rgba(0,0,0,.25);
    display: flex; flex-direction: column; align-items: center; justify-content: center; gap: 14px;
  }
  .badge__dot { width: 44px; height: 44px; border-radius: 50%; background: var(--orange); }
  .badge__name { color: #fff; font-family: "Jost", sans-serif; font-weight: 500; font-size: 26px; letter-spacing: 3px; }

  .where { position: absolute; top: 662px; left: 0; width: 100%; text-align: center; }
  .where__label { font-family: "Oswald", sans-serif; font-weight: 500; font-size: 33px; color: var(--orange); line-height: 1.1; }
  .where__address { margin-top: 6px; font-size: 18px; line-height: 1.45; color: var(--grey-text); }

  .vision { position: absolute; top: 790px; left: 80px; width: 547px; height: 190px; display: flex; }
  .vision__item { flex: 1; display: flex; flex-direction: column; align-items: center; }
  .vision__item + .vision__item { border-left: 1px solid var(--rule); }
  .vision__photo { width: 132px; height: 132px; border-radius: 50%; border: 4px solid #c8c8c8; }
  .vision__photo--prophetic { background: radial-gradient(circle at 50% 45%, var(--sky-glow), var(--sky-mid) 55%, var(--sky-dark)); }
  .vision__photo--worship { background: radial-gradient(circle at 50% 50%, #8a6a55, #4a3428 70%, #2c1f18); }
  .vision__photo--prayer { background: radial-gradient(circle at 45% 40%, #eadfd4, #c2a896 60%, #8d7565); }
  .vision__label { margin-top: 16px; font-family: "Oswald", sans-serif; font-size: 23px; color: var(--grey-label); letter-spacing: .5px; }

  .when {
    position: absolute; top: 1012px; left: 0; width: 100%; height: 58px;
    border-top: 1px solid var(--rule); border-bottom: 1px solid var(--rule);
    display: flex; align-items: center; justify-content: center; gap: 8px;
    font-size: 18px; color: var(--grey-text);
  }
  .when__label { font-family: "Oswald", sans-serif; font-weight: 500; font-size: 25px; color: var(--orange); }
  .when__year { color: var(--orange); }
  .when__sep { width: 2px; height: 24px; background: var(--orange); margin: 0 4px; }

  .site { position: absolute; top: 1098px; left: 0; width: 100%; display: flex; justify-content: center; align-items: center; gap: 6px; font-size: 17px; color: var(--grey-text); }
  .site__dot { width: 16px; height: 16px; border-radius: 50%; border: 3px solid var(--orange); }
  .site__accent { color: var(--orange); }

  .footer-bar { position: absolute; left: 0; bottom: 14px; width: 100%; height: 6px; background: var(--orange); }
</style>
</head>
<body>
<main class="flyer">
  <header class="hero">
    <svg width="707" height="560" viewBox="0 0 707 560">
      <defs>
        <linearGradient id="sky" x1="0" y1="0" x2="0" y2="1">
          <stop offset="0" stop-color="#3b2416"/>
          <stop offset="0.45" stop-color="#8a5428"/>
          <stop offset="0.75" stop-color="#c98a48"/>
          <stop offset="1" stop-color="#1c120b"/>
        </linearGradient>
      </defs>
      <path class="hero__band" d="M0,0 H707 V312 A385 385 0 0 1 0 312 Z" fill="var(--orange)"/>
      <path class="hero__photo" role="img" aria-label="Silhouettes of raised hands and crosses against a glowing sunset sky" d="M0,0 H707 V288 A380 380 0 0 1 0 288 Z" fill="url(#sky)"/>
    </svg>
    <h1 class="hero__title">HARVEST LANTERN<br>GATHERING 2018</h1>
  </header>

  <div class="badge">
    <span class="badge__dot"></span>
    <span class="badge__name">HLGCON</span>
  </div>

  <section class="where">
    <h2 class="where__label">WHERE</h2>
    <p class="where__address">Dunmore Community Center (Downtown Portland)<br>482 Willowby Street, Portland, ME 04117</p>
  </section>

  <section class="vision">
    <div class="vision__item">
      <div class="vision__photo vision__photo--prophetic" role="img" aria-label="Cupped hands holding the light of the setting sun"></div>
      <span class="vision__label">PROPHETIC</span>
    </div>
    <div class="vision__item">
      <div class="vision__photo vision__photo--worship" role="img" aria-label="Hands joined together in fellowship"></div>
      <span class="vision__label">WORSHIP</span>
    </div>
    <div class="vision__item">
      <div class="vision__photo vision__photo--prayer" role="img" aria-label="Folded hands resting on an open book in prayer"></div>
      <span class="vision__label">PRAYER</span>
    </div>
  </section>

  <section class="when">
    <span class="when__label">WHEN-</span>
    <span>August 24th, 25th &amp; 26th, <span class="when__year">2018</span></span>
    <span class="when__sep"></span>
    <span class="when__label">FROM-</span>
    <span>6:00PM</span>
  </section>

  <p class="site"><span class="site__dot"></span>www.<span class="site__accent">hlgcon2018</span>.org</p>

  <div class="footer-bar"></div>
</main>
</body>
</html>
```